Real Estate Development and Brokerage Middle East

Required is a web site design for a new branch of an existing Real Estate Development and Brokerage company. The Branch will be established in the United Arab Emirates - Corvalis Middle East, the mother company is based in Austria/Europe. The new branch focuses on the middle eastern clients such as Institutional Investors/Family Businesses/Wealthy Individuals looking either for a luxury home in Vienna City or the alpine nature or are interested to invest in ready made properties or real estate development projects in Austria run by the branches mother co. in Austria. The design should highlight both Services i.e. Investment for commercial purpose and for residential purposes (focus on the nature) as well as the companies focus on high end luxury selected properties only and having middle east experienced staff in the UAE.

The link to the Austrian HQ website is below: Design elements of that website might or might not be used, however the logo shall be the same.
http://brindlemock.example/QW7ZTRXLM

Attached the logo and a rough first draft of the structure of the website (not yet set in stone) . The attachment contains also a link to a website of a company in a similar industry. I do like the way they present the highlights on their start/home page. The boxes. By the way, we believe that more graphic (pictures) and a bit less text might be a good way to approach our future target customers.

As we hope to sell many of the projects and hence many new projects descriptions/pictures will be uploaded in future on an ongoing basis the page should have the ability to upload information and pics by our team (none of it is a web designer and has experience exceeding MS-Office).

Lastly - and for the future we might need (not sure yet) need the entire context in Arabic (the language button)

Thanks.
Olaf

Target Market(s)

Institutional Investors and wealthy individuals / family offices

Industry/Entity Type

Real Estate

Coding

Number of Pages Required

Requirements
Must have
• Same Logo as Parent Company
Nice to have
• News ticker/banner, high resolution picture heavy, changing pictures on start/home page, PDF downloads

```html
<!DOCTYPE html>
<html lang="en">
<head>
<meta charset="utf-8">
<title>Corvalis Middle East</title>
<link rel="stylesheet" href="https://fonts.googleapis.com/css2?family=Lato:wght@300;400&display=swap">
<style>
:root{
  --ink:#222;
  --nav:#444;
  --muted:#555;
  --white:#fff;
  --footer-bg:#e6e6e6;
  --search-bg:#d3d3d3;
  --icon-line:#8a8a8a;
  --brand:#5f7f98;
}
*{box-sizing:border-box;margin:0;padding:0}
html,body{width:1102px;height:1200px;overflow:hidden;background:var(--white)}
body{position:relative;font-family:"Lato",Arial,sans-serif;color:var(--ink)}
.site-header{position:absolute;left:0;top:0;width:1102px;height:93px;background:var(--white)}
.brand{position:absolute;left:64px;top:30px;display:flex;align-items:center;gap:8px}
.brand-mark{width:16px;height:16px;border-radius:50%;background:var(--brand)}
.brand-name{font-size:18px;font-weight:400;color:var(--brand)}
.utility-links{position:absolute;right:49px;top:27px;font-size:13.5px;color:var(--nav);font-weight:400}
.main-nav{position:absolute;left:605px;top:50px;display:flex;align-items:center;font-size:13.5px;color:var(--nav)}
.main-nav a{color:inherit;text-decoration:none;margin-right:36px}
.main-nav a.contact{margin-right:18px}
.menu-toggle{display:flex;align-items:center;gap:12px}
.hero{position:absolute;left:0;top:93px;width:1102px;height:534px;
  background:
   radial-gradient(ellipse at 75% 75%,rgba(40,35,30,.85),transparent 60%),
   radial-gradient(ellipse at 8% 70%,rgba(60,90,40,.9),transparent 45%),
   linear-gradient(180deg,#1e4a6a 0%,#2f6f8f 22%,#3c6e78 38%,#4a5a50 55%,#3a3a32 75%,#2c3526 100%)}
.hero-title{position:absolute;left:0;width:100%;top:178px;text-align:center;font-size:45px;font-weight:400;color:var(--white)}
.hero-lead{position:absolute;left:260px;width:582px;top:254px;text-align:center;font-size:20px;line-height:24px;font-weight:300;color:var(--white)}
.hero-btn{position:absolute;top:414px;width:267px;height:48px;border-radius:3px;display:flex;align-items:center;justify-content:center;font-size:20px;font-weight:400}
.btn-commercial{left:262px;border:1px solid var(--white);color:var(--white)}
.btn-residential{left:566px;background:var(--white);color:var(--ink)}
.about{position:absolute;left:300px;top:672px;width:500px;text-align:center}
.about h1{font-size:24px;font-weight:400;line-height:30px}
.about p{font-size:13px;line-height:16.8px;font-weight:400}
.about .more{margin-top:17px;font-size:13px;letter-spacing:.2px}
.site-footer{position:absolute;left:0;top:888px;width:1102px;height:312px;background:var(--footer-bg)}
.footer-col{position:absolute;top:63px;list-style:none;font-size:13.5px;line-height:22px;color:var(--muted)}
.col-a{left:190px}.col-b{left:435px}
.social{position:absolute;left:675px;top:68px;display:flex;gap:21px}
.social span{width:30px;height:30px;border-radius:50%;border:2px solid var(--icon-line)}
.search{position:absolute;left:672px;top:114px;width:224px;height:39px;border-radius:4px;background:var(--search-bg)}
.search svg{position:absolute;right:10px;top:10px}
.copyright{position:absolute;left:0;width:100%;top:269px;text-align:center;font-size:12px;color:var(--muted)}
</style>
</head>
<body>
<header class="site-header">
  <div class="brand"><span class="brand-mark"></span><span class="brand-name">Corvalis Immobilien</span></div>
  <div class="utility-links">Need help? | Newsletter</div>
  <nav class="main-nav">
    <a href="#">Home</a><a href="#">Properties</a><a href="#">Services &amp; news</a><a class="contact" href="#">Contact us</a>
    <span class="menu-toggle">
      <svg width="21" height="14" viewBox="0 0 21 14"><rect y="0" width="21" height="2" fill="#444"/><rect y="6" width="21" height="2" fill="#444"/><rect y="12" width="21" height="2" fill="#444"/></svg>
      Menu
    </span>
  </nav>
</header>

<section class="hero" role="img" aria-label="Alpine lakeside village with church spire, wooden roofs and flowering gardens">
  <h2 class="hero-title">We are building communities.</h2>
  <p class="hero-lead">Are you an Institutional Investor interested to invest in ready mage properties in Austria? Are you looking for a luxury home in Vienna? Are willing to be part of real estate development projects in Austira? Welcome! You are in the right corner.</p>
  <a class="hero-btn btn-commercial">Commercial</a>
  <a class="hero-btn btn-residential">Residential</a>
</section>

<section class="about">
  <h1>Corvalis Middle East</h1>
  <p>We are a Real estate Development and Brokerage company. The Branch will be established in the United Arab Emirates - Corvalis Middle East, the mother company is based in Austria/Europe. The new branch focuses on the middle eastern clients such as Institutional Investors/Family Businesses/Wealthy Individuals looking either for a luxury home in Vienna City or the alpine nature or are interested to invest in ready made properties or real estate development projects in Austria run by the branches mother co. in Austria.</p>
  <p class="more">+ KNOW MORE ABOUT OUR COMPANY.</p>
</section>

<footer class="site-footer">
  <ul class="footer-col col-a"><li>About us</li><li>Properties</li><li>Services &amp; News</li><li>References</li><li>Contact us</li></ul>
  <ul class="footer-col col-b"><li>Invest</li><li>News/Press</li><li>Our Customers</li><li>Team</li></ul>
  <div class="social"><span></span><span></span><span></span></div>
  <div class="search">
    <svg width="18" height="18" viewBox="0 0 18 18"><circle cx="7" cy="7" r="5.5" fill="none" stroke="#333" stroke-width="2"/><line x1="11" y1="11" x2="16" y2="16" stroke="#333" stroke-width="2.2" stroke-linecap="round"/></svg>
  </div>
  <p class="copyright">© All rights are reserved to Corvalis Immobilien</p>
</footer>
</body>
</html>
```